The Verdant Ledger App - Modernization & Graphics User Interface Friendliness Updates

We are Verdant Ledger, and we want to bring a new branding look and graphical user interface to the Verdant Ledger App. The app is a quick reference encyclopedia for all things produce. Boasting articles on over 2,000 produce items, with information ranging from taste and application to geographical and cultural significance. Included in its features are over 10 thousand recipes, and the Verdant Ledger App Harvest Circle – a global initiative to connect farmer, customer, and chef in one sustainable and easy to use application. The design needs to bring a greater sense of social connection – encouraging the user to participate in the 'Harvest Circled' experience voluntarily. The design should reflect a sense of authority reflecting the authenticity and reliability of the provided information, it's writing, and its sources. Download the App here: vledgr.example/install

Target Market(s)

Women and Men between ages 21-55.

Industry/Entity Type

Education

Font styles to use
Serif
Sans Serif

Colors

Designer to choose colors to be used in the design.

Requirements
Must have
• An updated user interface, the intuitive usability of the app is currently non-existent. We are looking to reflect as the authority on produce. The app design must reflect a professional, user-friendly, up-to-date, and trustworthy feel.
Nice to have
• To incorporate the social draw of the Harvest Circle we would like to include on the home page "Social Bubbles" (think Pictoloop stories) which updates with shared photos of produce and their location.
Should not have
• An overly complicated theme, distracting or unprofessional colors, and images.

```html
<!DOCTYPE html>
<html lang="en">
<head>
<meta charset="utf-8">
<title>Verdant Ledger – Categories</title>
<link href="https://fonts.googleapis.com/css2?family=Inter:wght@400;500;600&display=swap" rel="stylesheet">
<style>
  :root{
    --page:#121212;
    --brand:#00b52a;
    --on-brand:#ffffff;
    --list-bg:#eceff2;
    --divider:#d9dde1;
    --row-text:#3b4046;
    --chevron:#a3a8ae;
    --tab-bg:#ffffff;
    --tab-idle:#8f9398;
    --badge:#e0231c;
  }
  *{box-sizing:border-box;margin:0;padding:0}
  html,body{width:1200px;height:1200px;overflow:hidden;background:var(--page)}
  body{font-family:"Inter",sans-serif;position:relative}
  .screen{position:absolute;left:287px;top:42px;width:626px;height:1115px;background:var(--list-bg);overflow:hidden;display:flex;flex-direction:column}
  .app-header{background:var(--brand);color:var(--on-brand);height:110px;flex:none;position:relative}
  .status-bar{height:43px;display:flex;align-items:center;justify-content:space-between;padding:0 14px 0 16px;font-size:18px}
  .status-left,.status-right{display:flex;align-items:center;gap:6px;width:200px}
  .status-right{justify-content:flex-end}
  .signal{display:flex;gap:2px}
  .signal i{width:9px;height:9px;border-radius:50%;border:1.3px solid var(--on-brand)}
  .signal i.on{background:var(--on-brand)}
  .battery{width:36px;height:14px;border:1.5px solid var(--on-brand);border-radius:3px;padding:1.5px;position:relative}
  .battery::before{content:"";display:block;height:100%;background:var(--on-brand);border-radius:1px}
  .battery::after{content:"";position:absolute;right:-4px;top:3px;width:2px;height:5px;background:var(--on-brand);border-radius:0 1px 1px 0}
  .nav-bar{position:relative;height:67px;display:flex;align-items:center;justify-content:center}
  .nav-title{text-align:center;line-height:1}
  .nav-title h1{font-weight:400;font-size:26px;margin-top:-8px}
  .nav-title p{font-size:14px;margin-top:6px}
  .nav-menu{position:absolute;left:14px;top:22px}
  .nav-search{position:absolute;right:18px;top:18px}
  .category-list{list-style:none;flex:1;overflow:hidden}
  .category{height:98px;display:flex;align-items:center;border-bottom:1px solid var(--divider);padding:0 14px}
  .thumb{width:72px;height:72px;border-radius:50%;flex:none;box-shadow:0 1px 2px rgba(0,0,0,.15)}
  .category-name{flex:1;margin-left:26px;font-size:25px;color:var(--row-text);font-weight:400}
  .chevron{flex:none}
  .tab-bar{height:83px;flex:none;background:var(--tab-bg);border-top:1px solid var(--divider);display:flex}
  .tab{flex:1;display:flex;flex-direction:column;align-items:center;justify-content:flex-end;padding-bottom:8px;font-size:11.5px;font-weight:500;color:var(--tab-idle);letter-spacing:.2px}
  .tab.active{color:var(--brand)}
  .tab-icon{height:46px;display:flex;align-items:center;justify-content:center;position:relative}
  .badge{position:absolute;right:-14px;top:2px;background:var(--badge);color:#fff;font-size:10px;border-radius:9px;min-width:20px;height:18px;display:flex;align-items:center;justify-content:center;border:1.5px solid #fff}
</style>
</head>
<body>
<main class="screen">
  <header class="app-header">
    <div class="status-bar">
      <div class="status-left">
        <span class="signal"><i class="on"></i><i class="on"></i><i class="on"></i><i></i><i></i></span>
        <span>LUMA</span>
        <svg width="20" height="15" viewBox="0 0 20 15" fill="none" stroke="#fff" stroke-width="2"><path d="M2 5a12 12 0 0 1 16 0M5 8.5a7 7 0 0 1 10 0"/><circle cx="10" cy="12" r="1.6" fill="#fff" stroke="none"/></svg>
      </div>
      <span>4:21 PM</span>
      <div class="status-right">
        <span>100%</span>
        <span class="battery"></span>
      </div>
    </div>
    <div class="nav-bar">
      <svg class="nav-menu" width="28" height="22" viewBox="0 0 28 22" stroke="#fff" stroke-width="2.4"><path d="M1 3h26M1 11h26M1 19h26"/></svg>
      <div class="nav-title">
        <h1>Categories</h1>
        <p>Last updated Desember 18, 2014</p>
      </div>
      <svg class="nav-search" width="28" height="28" viewBox="0 0 28 28" fill="none" stroke="#fff" stroke-width="2.2"><circle cx="12" cy="12" r="9"/><path d="M18.5 18.5l7 7"/></svg>
    </div>
  </header>

  <ul class="category-list">
    <li class="category"><span class="thumb" role="img" aria-label="Assorted fresh fruit" style="background:radial-gradient(circle at 40% 40%,#f2b400,#d8361c 60%,#5a8f1e)"></span><span class="category-name">All Fruit</span><svg class="chevron" width="12" height="26" viewBox="0 0 12 26" fill="none" stroke="#a3a8ae" stroke-width="1.5"><path d="M2 2l8 11-8 11"/></svg></li>
    <li class="category"><span class="thumb" role="img" aria-label="Assorted fresh vegetables" style="background:radial-gradient(circle at 50% 45%,#e9eadf,#5f9c2c 55%,#e86a1e)"></span><span class="category-name">All Vegetables</span><svg class="chevron" width="12" height="26" viewBox="0 0 12 26" fill="none" stroke="#a3a8ae" stroke-width="1.5"><path d="M2 2l8 11-8 11"/></svg></li>
    <li class="category"><span class="thumb" role="img" aria-label="Foraged wild berries" style="background:radial-gradient(circle at 50% 50%,#8a2030,#2b2040 55%,#a63a2a)"></span><span class="category-name">Foraged</span><svg class="chevron" width="12" height="26" viewBox="0 0 12 26" fill="none" stroke="#a3a8ae" stroke-width="1.5"><path d="M2 2l8 11-8 11"/></svg></li>
    <li class="category"><span class="thumb" role="img" aria-label="Asian specialty produce" style="background:radial-gradient(circle at 45% 50%,#e9a03a,#4f7a22 55%,#3a2418)"></span><span class="category-name">Asian Specialties</span><svg class="chevron" width="12" height="26" viewBox="0 0 12 26" fill="none" stroke="#a3a8ae" stroke-width="1.5"><path d="M2 2l8 11-8 11"/></svg></li>
    <li class="category"><span class="thumb" role="img" aria-label="Indian specialty produce" style="background:radial-gradient(circle at 50% 50%,#e4c23a,#6e9b2a 50%,#c2301e)"></span><span class="category-name">Indian Specialties</span><svg class="chevron" width="12" height="26" viewBox="0 0 12 26" fill="none" stroke="#a3a8ae" stroke-width="1.5"><path d="M2 2l8 11-8 11"/></svg></li>
    <li class="category"><span class="thumb" role="img" aria-label="Latin specialty produce" style="background:radial-gradient(circle at 60% 60%,#f4a21c,#d6301e 55%,#f3e7d8)"></span><span class="category-name">Latin Specialties</span><svg class="chevron" width="12" height="26" viewBox="0 0 12 26" fill="none" stroke="#a3a8ae" stroke-width="1.5"><path d="M2 2l8 11-8 11"/></svg></li>
    <li class="category"><span class="thumb" role="img" aria-label="Japanese specialty produce" style="background:radial-gradient(circle at 50% 50%,#c43a22,#6b1e2a 55%,#2e5a1c)"></span><span class="category-name">Japaness Specialties</span><svg class="chevron" width="12" height="26" viewBox="0 0 12 26" fill="none" stroke="#a3a8ae" stroke-width="1.5"><path d="M2 2l8 11-8 11"/></svg></li>
    <li class="category"><span class="thumb" role="img" aria-label="Red apples" style="background:radial-gradient(circle at 45% 55%,#c81e24,#e86a5a 55%,#ffffff 80%)"></span><span class="category-name">Apples</span><svg class="chevron" width="12" height="26" viewBox="0 0 12 26" fill="none" stroke="#a3a8ae" stroke-width="1.5"><path d="M2 2l8 11-8 11"/></svg></li>
    <li class="category"><span class="thumb" role="img" aria-label="Oranges with leaves" style="background:radial-gradient(circle at 45% 55%,#f28a12,#f6b45a 50%,#ffffff 78%)"></span><span class="category-name">Orange</span><svg class="chevron" width="12" height="26" viewBox="0 0 12 26" fill="none" stroke="#a3a8ae" stroke-width="1.5"><path d="M2 2l8 11-8 11"/></svg></li>
    <li class="category"><span class="thumb" role="img" aria-label="Avocados" style="background:radial-gradient(circle at 45% 55%,#3a4a1e,#8aa050 50%,#ffffff 80%)"></span><span class="category-name"></span></li>
  </ul>

  <nav class="tab-bar">
    <div class="tab active"><span class="tab-icon"><svg width="34" height="40" viewBox="0 0 34 40"><path d="M17 12c-3-2-9-3-12 1s-3 12 1 18 8 8 11 6c3 2 7 0 11-6s4-14 1-18-9-3-12-1z" fill="#00b52a"/><path d="M17 12c0-4 2-8 5-10" stroke="#00b52a" stroke-width="2.4" fill="none"/></svg></span>PRODUCE</div>
    <div class="tab"><span class="tab-icon"><svg width="34" height="34" viewBox="0 0 34 34"><circle cx="17" cy="17" r="13" fill="none" stroke="#8f9398" stroke-width="1.6"/></svg></span>MURMUR</div>
    <div class="tab"><span class="tab-icon"><svg width="40" height="24" viewBox="0 0 40 24" fill="none" stroke="#8f9398" stroke-width="1.6"><path d="M2 12C8 4 32 4 38 12 32 20 8 20 2 12z"/><circle cx="20" cy="12" r="5.5"/><circle cx="20" cy="12" r="2"/></svg><span class="badge">42</span></span>SPOTTED</div>
    <div class="tab"><span class="tab-icon"><svg width="30" height="38" viewBox="0 0 30 38" fill="none" stroke="#8f9398" stroke-width="1.6"><rect x="2" y="2" width="26" height="34" rx="2"/><path d="M2 30h26"/><path d="M10 10a5 5 0 0 1 10 0v6H10z"/></svg></span>RECIPES</div>
    <div class="tab"><span class="tab-icon"><svg width="40" height="12" viewBox="0 0 40 12" fill="none" stroke="#8f9398" stroke-width="1.5"><circle cx="6" cy="6" r="4"/><circle cx="20" cy="6" r="4"/><circle cx="34" cy="6" r="4"/></svg></span>MORE</div>
  </nav>
</main>
</body>
</html>
```